Identidad Corporativa / Corporate Identity for Proposal Document

Crear una identidad corporativa para una propuesta de negocio. El documento debe estar dividió en Portada, Carta de Presentación, Contenido, Perfil Corporativo, Vision, Misión, Nuestros Servicios, Situación actual en el cliente, Nuestras Recomendaciones, Metodología de trabajo, Propuesta de Negocio, Términos de Pago, Aceptación del Propuesta. Proveer documento en formato Word.

Create a corporate Identity for a Business Proposal Standard. The table of contest will have Cover, Presentation Letter, Table of Content, Corporate Info, Vision, Mission, Our Services, Customer Situation, Our Recommendations, Methodology of Work, Business Proposal, Payment Terms, Acceptance.

Provide document Word format.

```html
<!DOCTYPE html>
<html lang="es">
<head>
<meta charset="utf-8">
<title>Propuesta de Consultoría – Identidad Corporativa</title>
<link rel="stylesheet" href="https://fonts.googleapis.com/css2?family=Montserrat:wght@700&family=Arimo:wght@400;700&display=swap">
<style>
  :root{
    --canvas:#e4eaf0;
    --navy:#1f3763;
    --ink:#1a1a1a;
    --brand:#243f73;
    --accent:#6fbf3a;
    --page-shadow:rgba(30,50,70,.35);
  }
  *{box-sizing:border-box;margin:0;padding:0}
  html,body{width:1200px;height:510px;overflow:hidden;background:var(--canvas)}
  .spread{position:relative;width:1200px;height:510px}
  .page{position:absolute;top:5px;width:383px;height:499px;overflow:hidden;box-shadow:0 0 4px var(--page-shadow);border:1px solid #8aa3b5}
  .page--cover{left:14px}
  .page--letter{left:406px}
  .page--contents{left:797px}
  .page__bg{position:absolute;inset:0;width:100%;height:100%}
  .brand{position:absolute;top:40px;display:flex;align-items:center;gap:5px;font-family:"Arimo",sans-serif;font-weight:700;color:var(--brand);text-transform:uppercase;line-height:1}
  .brand__dot{width:10px;height:10px;border-radius:50%;background:var(--accent)}
  .page--cover .brand{left:0;right:0;justify-content:center;font-size:14px;top:48px}
  .page--letter .brand,.page--contents .brand{right:28px;top:38px;font-size:10px}
  .cover-title{position:absolute;left:14px;right:14px;top:222px;text-align:center;font-family:"Montserrat",sans-serif;font-weight:700;font-size:14.5px;line-height:19px;color:var(--navy);text-transform:uppercase;letter-spacing:.2px;text-shadow:1px 1px 1px rgba(255,255,255,.8)}

  .letter p{position:absolute;left:57px;width:273px;top:var(--y);font-family:"Arimo",sans-serif;font-size:8.6px;line-height:9.8px;color:var(--ink);text-align:justify}

  .contents{font-family:"Arimo",sans-serif;color:var(--ink)}
  .contents__title{position:absolute;left:55px;top:80px;font-size:12.5px;font-weight:700}
  .toc{list-style:none}
  .toc li{position:absolute;left:55px;right:52px;top:var(--y);display:flex;align-items:baseline;white-space:nowrap;line-height:1}
  .toc .toc__leader{flex:1;border-bottom:1px dotted #333;margin:0 1px;transform:translateY(-1px)}
  .toc .lvl1{font-weight:700;font-size:6.8px}
  .toc .lvl2{font-size:5.2px;font-weight:700;padding-left:14px}
  .toc .lvl2 .toc__num{display:inline-block;width:15px}
  .toc .lvl2 > span:last-child{font-size:6px}
  .toc .lvl3{font-size:4.8px;padding-left:24px}
  .toc .lvl3 > span:last-child{font-size:6px}
</style>
</head>
<body>
<main class="spread">

  <section class="page page--cover">
    <svg class="page__bg" viewBox="0 0 383 499" preserveAspectRatio="none" aria-hidden="true">
      <defs>
        <linearGradient id="coverGreen" x1="0" y1="0" x2="1" y2="1">
          <stop offset="0" stop-color="#2da65a"/>
          <stop offset=".55" stop-color="#5ec98a"/>
          <stop offset="1" stop-color="#b5ead0"/>
        </linearGradient>
        <linearGradient id="coverWhite" x1="0" y1="0" x2="1" y2="1">
          <stop offset="0" stop-color="#f4fbf8"/>
          <stop offset="1" stop-color="#d9f1ec"/>
        </linearGradient>
        <linearGradient id="coverBlue" x1="0" y1="0" x2="1" y2="1">
          <stop offset="0" stop-color="#b9d3f0"/>
          <stop offset=".6" stop-color="#5b8fd0"/>
          <stop offset="1" stop-color="#1d6a86"/>
        </linearGradient>
      </defs>
      <rect width="383" height="499" fill="url(#coverGreen)"/>
      <path d="M0,398 C110,250 250,165 383,158 L383,499 L0,499 Z" fill="url(#coverWhite)"/>
      <path d="M115,499 C215,430 320,335 383,250 L383,499 Z" fill="url(#coverBlue)"/>
      <rect x="19" y="30" width="346" height="460" fill="#ffffff" opacity=".22"/>
      <rect x="19" y="30" width="346" height="56" fill="#ffffff" opacity=".35"/>
    </svg>
    <div class="brand"><span class="brand__dot"></span>Brightway Systems</div>
    <h1 class="cover-title">Propuesta de Consultoría,<br>Mantenimiento y Desarrollo<br>de Sistemas</h1>
  </section>

  <section class="page page--letter">
    <svg class="page__bg" viewBox="0 0 383 499" preserveAspectRatio="none" aria-hidden="true">
      <defs>
        <linearGradient id="letterGreen" x1="0" y1="0" x2="1" y2="1">
          <stop offset="0" stop-color="#8fd9ac"/>
          <stop offset="1" stop-color="#d6f3e4"/>
        </linearGradient>
        <linearGradient id="letterBlue" x1="0" y1="0" x2="1" y2="1">
          <stop offset="0" stop-color="#dbe8f7"/>
          <stop offset="1" stop-color="#8fb6e2"/>
        </linearGradient>
      </defs>
      <rect width="383" height="499" fill="url(#letterGreen)"/>
      <path d="M0,345 C100,220 250,150 383,140 L383,499 L0,499 Z" fill="#f3fbf8"/>
      <path d="M110,499 C215,430 320,335 383,245 L383,499 Z" fill="url(#letterBlue)"/>
      <rect x="19" y="30" width="346" height="460" fill="#ffffff" opacity=".28"/>
      <rect x="19" y="30" width="346" height="56" fill="#ffffff" opacity=".4"/>
    </svg>
    <div class="brand"><span class="brand__dot"></span>Brightway Systems</div>
    <div class="letter">
      <p style="--y:128px">De nuestra mayor consideración:</p>
      <p style="--y:159px">Por la presente nos dirigimos a usted con la propuesta de Consultoría, Programación y Servicios.</p>
      <p style="--y:190px">Brightway Systems, Inc. provee toda su experiencia de más de 27 años en el área de sistemas de información y desarrollo de aplicaciones.</p>
      <p style="--y:231px">Finalmente, le agradezco la oportunidad que nos brindan de presentarle nuestra propuesta.</p>
      <p style="--y:267px">Atentamente,</p>
      <p style="--y:311px">Marcos L. Ortega Vidal</p>
      <p style="--y:326px">Presidente</p>
    </div>
  </section>

  <section class="page page--contents">
    <svg class="page__bg" viewBox="0 0 383 499" preserveAspectRatio="none" aria-hidden="true">
      <defs>
        <linearGradient id="tocGreen" x1="0" y1="0" x2="1" y2="1">
          <stop offset="0" stop-color="#8fd9ac"/>
          <stop offset="1" stop-color="#d6f3e4"/>
        </linearGradient>
        <linearGradient id="tocBlue" x1="0" y1="0" x2="1" y2="1">
          <stop offset="0" stop-color="#dbe8f7"/>
          <stop offset="1" stop-color="#8fb6e2"/>
        </linearGradient>
      </defs>
      <rect width="383" height="499" fill="url(#tocGreen)"/>
      <path d="M0,410 C100,260 250,165 383,155 L383,499 L0,499 Z" fill="#f3fbf8"/>
      <path d="M110,499 C215,430 320,335 383,250 L383,499 Z" fill="url(#tocBlue)"/>
      <rect x="19" y="30" width="346" height="460" fill="#ffffff" opacity=".28"/>
      <rect x="19" y="30" width="346" height="56" fill="#ffffff" opacity=".4"/>
    </svg>
    <div class="brand"><span class="brand__dot"></span>Brightway Systems</div>
    <div class="contents">
      <h2 class="contents__title">Contenido</h2>
      <ul class="toc">
        <li class="lvl1" style="--y:126px"><span>Perfil Corporativo</span><span class="toc__leader"></span><span>4</span></li>
        <li class="lvl1" style="--y:137px"><span>Descripción de los Servicios</span><span class="toc__leader"></span><span>5</span></li>
        <li class="lvl2" style="--y:154px"><span><span class="toc__num">1.1</span>Consultoría</span><span class="toc__leader"></span><span>7</span></li>
        <li class="lvl2" style="--y:168px"><span><span class="toc__num">1.2</span>Soluciones de Redes</span><span class="toc__leader"></span><span>7</span></li>
        <li class="lvl2" style="--y:183px"><span><span class="toc__num">1.3</span>Desarrollo de Aplicaciones</span><span class="toc__leader"></span><span>8</span></li>
        <li class="lvl3" style="--y:191px"><span>1.3.1 Metodología de Proyectos</span><span class="toc__leader"></span><span>9</span></li>
        <li class="lvl2" style="--y:205px"><span><span class="toc__num">1.4</span>Plataforma de Internet</span><span class="toc__leader"></span><span>10</span></li>
        <li class="lvl2" style="--y:220px"><span><span class="toc__num">1.5</span>Desarrollo Multimedia</span><span class="toc__leader"></span><span>10</span></li>
        <li class="lvl2" style="--y:235px"><span><span class="toc__num">1.6</span>Mantenimiento</span><span class="toc__leader"></span><span>11</span></li>
        <li class="lvl1" style="--y:245px"><span>Compromiso y apoyo institucional para la ejecución del Proyecto</span><span class="toc__leader"></span><span>12</span></li>
        <li class="lvl1" style="--y:258px"><span>Equipo de trabajo</span><span class="toc__leader"></span><span>13</span></li>
        <li class="lvl1" style="--y:271px"><span>Propuesta de Negocio</span><span class="toc__leader"></span><span>14</span></li>
        <li class="lvl2" style="--y:288px"><span><span class="toc__num">1.1</span>Situación actual</span><span class="toc__leader"></span><span>14</span></li>
        <li class="lvl2" style="--y:303px"><span><span class="toc__num">1.2</span>Detalle de costos</span><span class="toc__leader"></span><span>16</span></li>
        <li class="lvl1" style="--y:313px"><span>Términos de Pago</span><span class="toc__leader"></span><span>16</span></li>
        <li class="lvl1" style="--y:325px"><span>Declaración de conformidad del cliente</span><span class="toc__leader"></span><span>17</span></li>
      </ul>
    </div>
  </section>

</main>
</body>
</html>
```